Lantern Petro - needs a business card

Lantern Petro is a U.S. based diesel sourcing and distribution company that supports American oil & gas fields through providing quality product and consistent services.

Target Market(s)

Oil and Gas

Contact Information for Business Card

The background of the card must be white to ensure the logo pops.

Font styles to use
Serif
Sans Serif

Colors

Designer to choose colors to be used in the design.

Requirements
Must have
• Front of Card: Tag line: Lantern Petro, Powering the Nation's Oil & Gas fields.
• Not sure if you guys do this part but just in case...
• Dale Winterholt
• Owner/CEO
• C:701.555.0148
• E:Dwinterholt@lanternpetro.com
• W:Lanternpetro.com
• Locations: Servicing the Powder River, DJ basin and Bakken formations.
• Back of Card: " Frac fueling is what we do. We understand how important diesel fuel is to your operation, which is why our main service line is Frac fueling. We assure our supply and stand by our service"

```html
<!DOCTYPE html>
<html lang="en">
<head>
<meta charset="utf-8">
<title>Lantern Petro – Business Card</title>
<link href="https://fonts.googleapis.com/css2?family=Lato:wght@400;700&family=Oswald:wght@600&display=swap" rel="stylesheet">
<style>
  :root {
    --navy: #1b2d5c;
    --navy-text: #1f3166;
    --red: #c8202f;
    --white: #ffffff;
    --grey: #5a5e66;
    --ink: #33363c;
    --rule: #6f7aa0;
    --backdrop: #e6e7ea;
  }
  * { box-sizing: border-box; margin: 0; padding: 0; }
  html, body { width: 1200px; height: 912px; overflow: hidden; }
  body {
    background: var(--backdrop);
    font-family: "Lato", Arial, sans-serif;
    position: relative;
  }
  .card {
    position: absolute;
    width: 600px;
    height: 343px;
    border-radius: 18px;
    box-shadow: 0 10px 28px rgba(0,0,0,.18);
    overflow: hidden;
  }
  /* Back of card */
  .card--back {
    left: 60px; top: 60px;
    background: var(--navy);
    color: var(--white);
    display: flex; flex-direction: column; align-items: center; justify-content: center;
    text-align: center;
    gap: 34px;
  }
  .brand {
    display: flex; align-items: center; gap: 12px;
    font-weight: 700;
    font-size: 34px;
    letter-spacing: 1px;
    color: var(--white);
  }
  .brand__dot {
    width: 26px; height: 26px; border-radius: 50%;
    background: var(--red);
  }
  .mission {
    font-size: 16.5px;
    line-height: 1.35;
    max-width: 520px;
  }
  /* Front of card */
  .card--front {
    left: 540px; top: 509px;
    background: var(--white);
  }
  .identity {
    position: absolute; left: 30px; top: 74px;
    width: 270px;
    text-align: right;
  }
  .identity__name {
    font-family: "Oswald", "Arial Narrow", sans-serif;
    font-weight: 600;
    font-size: 34px;
    line-height: 1;
    color: var(--navy-text);
    text-transform: uppercase;
    letter-spacing: .5px;
    white-space: nowrap;
  }
  .identity__role {
    margin-top: 6px;
    font-size: 16px;
    color: var(--grey);
  }
  .divider {
    position: absolute; left: 316px; top: 58px;
    width: 1px; height: 86px;
    background: var(--ink);
  }
  .contacts {
    position: absolute; left: 332px; top: 62px; right: 24px;
    list-style: none;
    font-size: 14px;
    color: var(--ink);
  }
  .contacts li { display: flex; align-items: center; gap: 8px; height: 26px; white-space: nowrap; }
  .contacts svg { width: 13px; height: 13px; flex: none; }
  .tagline {
    position: absolute; left: 40px; right: 40px; top: 200px;
    border-bottom: 1px solid var(--rule);
    padding-bottom: 10px;
    font-size: 16px;
    font-weight: 700;
    color: var(--navy-text);
  }
  .locations {
    position: absolute; left: 40px; right: 40px; top: 244px;
    font-size: 17.5px;
    color: var(--ink);
  }
</style>
</head>
<body>

<section class="card card--back" aria-label="Back of card">
  <div class="brand"><span class="brand__dot"></span>Lantern Petro</div>
  <p class="mission">
    Frac fueling is what we do.<br>
    We understand how important diesel fuel is to your operation,<br>
    which is why our main service line is Frac fueling.<br>
    We assure our supply and stand by our service"
  </p>
</section>

<section class="card card--front" aria-label="Front of card">
  <div class="identity">
    <h1 class="identity__name">Dale Winterholt</h1>
    <p class="identity__role">Owner/CEO</p>
  </div>
  <div class="divider"></div>
  <ul class="contacts">
    <li>
      <svg viewBox="0 0 24 24" aria-hidden="true"><path fill="#1f3166" d="M6.6 10.8a15 15 0 0 0 6.6 6.6l2.2-2.2c.3-.3.7-.4 1-.2 1.1.4 2.3.6 3.6.6.6 0 1 .4 1 1V20c0 .6-.4 1-1 1A17 17 0 0 1 3 4c0-.6.4-1 1-1h3.5c.6 0 1 .4 1 1 0 1.3.2 2.5.6 3.6.1.3 0 .7-.2 1z"/></svg>
      701.555.0148
    </li>
    <li>
      <svg viewBox="0 0 24 24" aria-hidden="true"><rect x="2.5" y="5" width="19" height="14" rx="1.5" fill="none" stroke="#1f3166" stroke-width="2"/><path d="M3 6l9 7 9-7" fill="none" stroke="#1f3166" stroke-width="2"/></svg>
      Dwinterholt@lanternpetro.com
    </li>
    <li>
      <svg viewBox="0 0 24 24" aria-hidden="true"><circle cx="12" cy="12" r="9.5" fill="none" stroke="#1f3166" stroke-width="2"/><path d="M2.5 12h19M12 2.5c3 3 3 16 0 19M12 2.5c-3 3-3 16 0 19" fill="none" stroke="#1f3166" stroke-width="1.6"/></svg>
      www.lanternpetro.com
    </li>
  </ul>
  <p class="tagline">Lantern Petro, Powering the Nation's Oil &amp; Gas fields.</p>
  <p class="locations">Servicing the Powder River, DJ basin and Bakken formations.</p>
</section>

</body>
</html>
```